Our website, is loosely based on a grant proposal submitted to the Northfield Vascular Society last year for a community-based project that could improve the health of the community at large, I have attached this file for your review (underline "loosely). The idea is to create a "patient navigator" a website where patients can both learn and use as a resource for their care. I have been working on the project for some time, but my other responsibilities as a cardiologist have not allowed me time to learn and design a website of this type. Our website is intended for a spanish speaking audience and is in Spanish language. Designs in english will have to be translated. Our name: AcademiaBienestar.com: means a health university: One option is to have the website have a "university" theme. The project calls for: An initial: easy registration process: collecting name, DOB and city. Simplicity is key, many of our patients barely use computers, and this site is meant to make things easier, not complicate them. The web site should work as an extension of the doctors office, so it should be serious, creative, addictive, engaging. Doctors will see the patients in the office then refer them to the website to continue their learning about their conditions. There should be a page where patients can post questions: a panel of doctors: represented with their pictures, (in circles? around the question answered?) titles and small resumes (our "faculty") answers them. Every person that will attach themself to this website will have a title: doctors and nurses will be professors, residents and fellows will be assistant professors, aids can be PA?. The site should have a market place where people can purchase items that doctors recommend including foods, products and devices; here too, we can have a "bookshop". This should have a flexible mechanism for doctors to add their recommendations a patients can have access to them. Very important: there should be a site intended to be a classroom, this is the meat of this protect: where people can watch videos our staff will make to learn about different subjects; the site should keep track of the videos watched by the person and eventually "graduate them". These videos will be created by my staff, and added over time to the site, students should be able to "request" classes (videos). It should have a site where people can input their medications (notebook), have them stored and printed as a list if necessary. And finally it should have a contact and references section. We have set up a relationship with another site that help people count calories: and a link to this should be available. We have a link to our twitter account, This protect is intended to expand, and we hope to establish a long term relationship with the design team to expand it as needed in the future. The site is on PageHarbor and can be seen in its current form at AcademiaBienestar.com . We have had a logo designed with specific colors of the hospital I work with and one plan is to present it to our hospital to adopt our page in it final form. Again, this site is in spanish and intended for a spanish audience.

Target Market(s)

Spanish speaking, late 30s to early 60s audience.

Industry/Entity Type

Community

Number of Pages Required

4 page

Font styles to use
Sans Serif

Colors
a64599
fceff5
3277b5

Requirements
Must have
• A simple, accesible look
Nice to have
• Animations, moving parts
Should not have
• English

```html
<!DOCTYPE html>
<html lang="es">
<head>
<meta charset="utf-8">
<title>AcademiaBienestar</title>
<link rel="stylesheet" href="https://fonts.googleapis.com/css2?family=Roboto:wght@300;400;500;700&display=swap">
<style>
:root{
  --magenta:#a64599;
  --pink:#fceff5;
  --blue:#3277b5;
  --navy:#1f4e7c;
  --ink:#3a3a3a;
  --muted:#777;
  --white:#fff;
}
*{box-sizing:border-box;margin:0;padding:0}
html,body{width:1200px;height:2278px;overflow:hidden}
body{position:relative;font-family:'Roboto',Arial,sans-serif;color:var(--ink);background:var(--white)}
.abs{position:absolute}
.band{position:absolute;left:0;width:1200px}
.wordmark{font-family:'Roboto',Arial,sans-serif;font-weight:300;color:var(--navy);letter-spacing:-0.5px}
/* header */
.header{top:0;height:112px;background:var(--pink)}
.header .wordmark{left:171px;top:34px;font-size:40px}
.phone{left:858px;top:34px;font-size:12px;color:var(--muted)}
.phone strong{display:block;font-size:19px;font-weight:400;color:var(--magenta);margin-top:4px}
.phone svg{position:absolute;left:0;top:18px}
.phone .txt{margin-left:36px}
/* nav */
.nav{top:112px;height:55px;background:var(--blue)}
.nav ul{position:absolute;left:171px;top:0;display:flex;list-style:none;height:55px;border-left:1px solid rgba(255,255,255,.18)}
.nav li{width:111px;line-height:55px;text-align:center;color:#fff;font-size:13px;border-right:1px solid rgba(255,255,255,.18)}
.nav li.wide{width:126px}
.nav .social{position:absolute;left:868px;top:18px;display:flex;gap:14px}
.nav .social span{width:18px;height:18px;border-radius:50%;background:#fff;opacity:.9}
/* hero */
.hero{top:167px;height:346px;background:linear-gradient(90deg,#c9a58a 0%,#e9d8c8 35%,#f3efe9 60%,#e6ecef 100%)}
.hero-brand{left:173px;top:294px;width:290px;height:44px;background:rgba(255,255,255,.9);font-size:31px;padding:4px 10px}
.hero-tag{left:173px;top:344px;width:351px;height:46px;background:rgba(255,255,255,.9);color:var(--magenta);font-size:19px;line-height:46px;padding-left:19px}
.arrow{width:54px;height:54px;border-radius:50%;border:2px solid var(--magenta)}
.dots{left:578px;top:491px;display:flex;gap:5px}
.dots span{width:11px;height:11px;border-radius:50%;border:1.5px solid var(--magenta);background:#fff}
.dots span.on{background:var(--magenta)}
.quote{left:718px;top:200px;width:310px;height:290px;background:var(--navy);border:4px solid rgba(255,255,255,.35);color:#fff;padding:16px 22px}
.quote h2{font-size:25px;font-weight:400;text-align:center}
.quote p{font-size:10.5px;text-align:center;margin-top:6px;line-height:1.25}
.quote .field{height:27px;background:var(--magenta);margin:6px 0 0;font-size:10px;line-height:27px;padding-left:14px;font-weight:500}
.quote .field:first-of-type{margin-top:12px}
.quote .foot{display:flex;justify-content:space-between;align-items:center;margin-top:13px;font-size:10px;font-weight:500}
.quote .send{width:96px;height:29px;background:#fff;color:var(--blue);text-align:center;line-height:29px;font-size:12px}
/* cta bands */
.cta{height:98px;background:var(--blue)}
.cta p{position:absolute;left:173px;top:0;line-height:98px;color:#fff;font-size:22px}
.cta .btn{position:absolute;left:752px;top:25px;width:276px;height:49px;line-height:49px;background:var(--navy);color:#fff;text-align:center;font-size:17px}
/* welcome */
.welcome-title{left:173px;top:665px;font-size:26px;font-weight:400;color:var(--navy)}
.welcome-title .wordmark{font-size:29px}
.body-txt{font-size:11px;line-height:1.3;color:var(--ink)}
.btn-mag{background:var(--magenta);color:#fff;font-size:10px;text-align:center;font-weight:500}
.photo{background:linear-gradient(120deg,#e6e0d6,#c9c2b6)}
.play{width:54px;height:54px;border-radius:50%;background:rgba(40,40,40,.75);border:3px solid #ccc}
/* services */
.services{top:864px;height:327px;background:linear-gradient(90deg,#dfe7ec 0%,#eef3f6 40%,#dde8ef 100%)}
.services-title{left:627px;top:916px;font-size:35px;font-weight:400;color:var(--magenta)}
.svc-item{left:631px;font-size:16px;color:var(--navy)}
.svc-item svg{vertical-align:-2px;margin-right:10px}
/* classes */
.classes-title{left:448px;top:1236px;font-size:23px;font-weight:400;color:var(--blue)}
/* quick links */
.links{left:769px;top:1229px;width:259px;height:228px;background:var(--pink)}
.links h3{font-size:23px;font-weight:400;color:var(--magenta);padding:14px 0 8px 22px}
.links li{list-style:none;height:43px;line-height:43px;margin:0 14px;padding-left:8px;font-size:11px;color:var(--navy);border-bottom:1px solid #fff;position:relative}
.links li:last-child{border-bottom:0}
.links li svg{position:absolute;right:2px;top:15px}
/* features */
.features{top:1590px;height:285px;background:var(--pink)}
.feat .avatar{width:95px;height:95px;border-radius:50%;border:3px solid var(--magenta);background:linear-gradient(135deg,#d8c4b0,#8e9fb3)}
.feat h4{font-size:11px;color:var(--magenta);font-weight:500;margin-bottom:6px}
/* shops */
.shop{width:422px;height:171px;top:1907px}
.shop span{position:absolute;left:0;right:0;bottom:0;height:54px;background:rgba(255,255,255,.55);text-align:center;color:var(--blue);font-size:28px;line-height:54px}
/* footer */
.footer{top:2108px;height:120px;background:var(--pink)}
.footer .wordmark{left:171px;top:38px;font-size:40px}
.footer .social{position:absolute;left:894px;top:44px;display:flex;gap:10px}
.footer .social span{width:27px;height:27px;border-radius:50%;background:#b9b9b9}
.copy{top:2228px;height:50px;text-align:center;line-height:50px;font-size:13px;color:var(--muted)}
</style>
</head>
<body>

<header class="band header">
  <div class="abs wordmark">AcademiaBienestar</div>
  <div class="abs phone">
    <svg width="24" height="24" viewBox="0 0 24 24"><path d="M6 3l3 4-2 2c1 3 4 6 7 7l2-2 4 3-2 4C9 21 3 15 2 5z" fill="none" stroke="#a64599" stroke-width="2"/></svg>
    <div class="txt">¡Llámenos hoy!<strong>0800 (555) 0142</strong></div>
  </div>
</header>

<nav class="band nav">
  <ul>
    <li>INICIO</li><li>NOSOTROS</li><li>TIENDA</li><li>BLOG</li><li>PREGUNTAS</li><li class="wide">CONTACTO</li>
  </ul>
  <div class="social"><span></span><span></span><span></span><span></span></div>
</nav>

<section class="band hero" role="img" aria-label="Foto de una pareja sonriente mirando una tableta"></section>
<div class="abs hero-brand wordmark">AcademiaBienestar</div>
<div class="abs hero-tag">¡TU BIENESTAR EMPIEZA HOY!</div>
<div class="abs arrow" style="left:47px;top:315px"><svg width="50" height="50" viewBox="0 0 50 50"><path d="M28 17l-8 8 8 8" fill="none" stroke="#a64599" stroke-width="2"/></svg></div>
<div class="abs arrow" style="left:1083px;top:315px"><svg width="50" height="50" viewBox="0 0 50 50"><path d="M22 17l8 8-8 8" fill="none" stroke="#a64599" stroke-width="2"/></svg></div>
<div class="abs dots"><span class="on"></span><span></span><span></span></div>

<form class="abs quote">
  <h2>¡REGÍSTRATE AHORA!</h2>
  <p>Lorem ipsum dolor sit amet, consectetuer adipiscing elit, sed diam nonummy.</p>
  <div class="field">NOMBRE</div>
  <div class="field">CORREO</div>
  <div class="field">FECHA DE NACIMIENTO</div>
  <div class="field">CIUDAD</div>
  <div class="foot"><span>¡CONTÁCTANOS!</span><span class="send">ENVIAR</span></div>
</form>

<section class="band cta" style="top:513px">
  <p>¡CONTÁCTANOS Y MEJORA TU SALUD!</p>
  <div class="btn">PEDIR CITA AHORA</div>
</section>

<section class="welcome">
  <h2 class="abs welcome-title">Bienvenidos a <span class="wordmark">AcademiaBienestar</span></h2>
  <p class="abs body-txt" style="left:173px;top:706px;width:460px">Lorem ipsum dolor sit amet, consectetuer adipiscing elit, sed diam nonummy nibh euismod tincidunt ut laoreet dolore magna aliquam erat volutpat. Ut wisi enim ad minim veniam, quis nostrud exerci tation ullamcorper suscipit lobortis nisl ut aliquip ex ea commodo consequat. Duis autem vel eum iriure dolor in hendrerit in vulputate velit.</p>
  <div class="abs btn-mag" style="left:173px;top:767px;width:120px;height:35px;line-height:35px">LEER MÁS</div>
  <div class="abs photo" style="left:652px;top:644px;width:376px;height:184px" role="img" aria-label="Imagen de video de una enfermera atendiendo a una paciente mayor"></div>
  <div class="abs play" style="left:813px;top:709px"><svg width="48" height="48" viewBox="0 0 48 48"><path d="M19 14l14 10-14 10z" fill="#ddd"/></svg></div>
</section>

<section class="band services" role="img" aria-label="Foto de una doctora con una tableta en un pasillo luminoso de hospital"></section>
<h2 class="abs services-title">NUESTROS SERVICIOS</h2>
<div class="abs svc-item" style="top:975px"><svg width="16" height="14" viewBox="0 0 16 14"><path d="M2 1l6 6-6 6M8 1l6 6-6 6" fill="none" stroke="#a64599" stroke-width="2"/></svg>APRENDE A CUIDARTE</div>
<div class="abs svc-item" style="top:1005px"><svg width="16" height="14" viewBox="0 0 16 14"><path d="M2 1l6 6-6 6M8 1l6 6-6 6" fill="none" stroke="#a64599" stroke-width="2"/></svg>RECURSOS PARA PACIENTES</div>
<p class="abs body-txt" style="left:631px;top:1038px;width:400px">Lorem ipsum dolor sit amet, consectetuer adipiscing elit, sed diam nonummy nibh euismod tincidunt ut laoreet dolore magna aliquam erat volutpat. Ut wisi enim ad minim veniam, quis nostrud exerci tation ullamcorper suscipit...</p>
<div class="abs btn-mag" style="left:631px;top:1094px;width:121px;height:36px;line-height:36px">LEER MÁS</div>

<section class="classes">
  <div class="abs photo" style="left:171px;top:1227px;width:241px;height:232px;border:1px solid #ddd" role="img" aria-label="Foto de un médico conversando con una paciente en su escritorio"></div>
  <h2 class="abs classes-title">CLASES PARA ALUMNOS</h2>
  <p class="abs body-txt" style="left:448px;top:1270px;width:282px">Lorem ipsum dolor sit amet, consectetuer adipiscing elit, sed diam nonummy nibh euismod tincidunt ut laoreet dolore magna aliquam erat volutpat. Ut wisi enim ad minim veniam, quis nostrud exerci tation ullamcorper suscipit lobortis nisl ut aliquip ex ea commodo consequat. Duis autem vel eum iriure dolor in hendrerit in vulputate velit</p>
  <div class="abs photo" style="left:448px;top:1377px;width:114px;height:69px" role="img" aria-label="Miniatura de video de una clase"></div>
  <div class="abs play" style="left:490px;top:1396px;width:32px;height:32px;border-width:2px"><svg width="28" height="28" viewBox="0 0 28 28"><path d="M11 8l8 6-8 6z" fill="#ddd"/></svg></div>
  <div class="abs" style="left:576px;top:1403px;font-size:15px;color:#555">¡Mira los videos!</div>
  <div class="abs links">
    <h3>ENLACES RÁPIDOS</h3>
    <ul>
      <li>SOLICITAR CLASES<svg width="8" height="12" viewBox="0 0 8 12"><path d="M1 1l5 5-5 5" fill="none" stroke="#1f4e7c" stroke-width="1.5"/></svg></li>
      <li>NAVEGACIÓN DEL PACIENTE<svg width="8" height="12" viewBox="0 0 8 12"><path d="M1 1l5 5-5 5" fill="none" stroke="#1f4e7c" stroke-width="1.5"/></svg></li>
      <li>LIBRERÍA<svg width="8" height="12" viewBox="0 0 8 12"><path d="M1 1l5 5-5 5" fill="none" stroke="#1f4e7c" stroke-width="1.5"/></svg></li>
      <li>PREGUNTAS FRECUENTES<svg width="8" height="12" viewBox="0 0 8 12"><path d="M1 1l5 5-5 5" fill="none" stroke="#1f4e7c" stroke-width="1.5"/></svg></li>
    </ul>
  </div>
</section>

<section class="band cta" style="top:1493px">
  <p>¡PARA APRENDER, SOLICITA CLASES EN VIDEO!</p>
  <div class="btn">SOLICITAR CLASES</div>
</section>

<section class="band features"></section>
<div class="feat">
  <div class="abs avatar" style="left:173px;top:1624px" role="img" aria-label="Retrato de una paciente"></div>
  <div class="abs" style="left:283px;top:1646px;width:300px"><h4>LOREM IPSUM DOLOR SIT AMET, ?</h4><p class="body-txt">Lorem ipsum dolor sit amet, consectetuer adipiscing elit, diam nonummy nibhdf euismod tincidunt ut laoreet dolore.</p></div>
  <div class="abs avatar" style="left:631px;top:1624px" role="img" aria-label="Retrato de un paciente con una tableta"></div>
  <div class="abs" style="left:741px;top:1646px;width:290px"><h4>LOREM IPSUM DOLOR SIT AMET, ?</h4><p class="body-txt">Lorem ipsum dolor sit amet, consectetuer adipiscing elit, diam nonummy nibhdf euismod tincidunt ut laoreet dolore.</p></div>
  <div class="abs avatar" style="left:173px;top:1743px" role="img" aria-label="Retrato de una alumna"></div>
  <div class="abs" style="left:283px;top:1766px;width:300px"><h4>LOREM IPSUM DOLOR SIT AMET, ?</h4><p class="body-txt">Lorem ipsum dolor sit amet, consectetuer adipiscing elit, diam nonummy nibhdf euismod tincidunt ut laoreet dolore.</p></div>
  <div class="abs avatar" style="left:631px;top:1743px" role="img" aria-label="Retrato de un hombre sonriente"></div>
  <div class="abs" style="left:741px;top:1766px;width:290px"><h4>LOREM IPSUM DOLOR SIT AMET, ?</h4><p class="body-txt">Lorem ipsum dolor sit amet, consectetuer adipiscing elit, diam nonummy nibhdf euismod tincidunt ut laoreet dolore.</p></div>
</div>

<div class="abs shop" style="left:171px;background:linear-gradient(90deg,#9a8e86,#d8d2cc,#8c827a)" role="img" aria-label="Foto del interior de una librería"><span>LIBRERÍA</span></div>
<div class="abs shop" style="left:606px;background:linear-gradient(90deg,#c9a46a,#b98d6a,#d6c8b0)" role="img" aria-label="Foto de estantes de un mercado con alimentos"><span>MERCADO</span></div>

<footer class="band footer">
  <div class="abs wordmark">AcademiaBienestar</div>
  <div class="social"><span></span><span></span><span></span><span></span></div>
</footer>
<div class="band copy">Derechos reservados © 2014 AcademiaBienestar</div>

</body>
</html>
```